4 Banners Required for Credit Card Comparison website

Project:

Creation of online advertising banners for use on Quorvel AdLink network and for display advertising on PalHaven.com

Headline to appear on all banners:
Save up to $1,000 or more in interest with a Balance Transfer Credit Card. Compare the offers on (logo)

Formats
- 728 x 90
- 468 x 60
- 300 x 250
- 160 x 600

Background:

Card Match Scout (http://www.cardmatchscout.example.au) is a credit card comparison service that compares the best credit cards in the Australian market. It helps consumers to find the right credit card for them. CMS want to attract more people to our site to compare and apply for credit cards online. The primary focus is for customers to compare the card offers on our comparison tables and apply online as opposed to going to a bank, calling or going to the bank site directly.

Desired Outcomes:
1. Viewers click on the banner and go through to Card Match Scout
2. New people click on the banner ad and go to our website, compare the cards and apply online
3. Get people to subscribe to our credit card email alert service

Note: Would prefer to have banners ASAP (sooner than 5 days if possible). Designers who act on it quickly, and supply great designs will most likely be awarded the winner
Updates

Thanks for the great work so far - we are really liking the submissions :)

Question - does anyone that has submitted a design so far have the ability to create flash banners? We are also considering our options as we have heard that flash banners are sometimes more effective

Cheers

Tobias

Target Market(s)

- Australian Credit Card users
- 18+ male and female
- Savvy people wanting a better deal on their credit card

Industry/Entity Type

Credit Card

Requirements
Must have
• - Need to quickly explain the simple concept that the website provides.
- Don’t want to use metaphors, prefer to use screenshots of the comparison table
- Simple 1 line headline with an easy call to action
Nice to have
• - Suggest different headline to the one we''ve proposed
Should not have
• The design should not use old-style, serif fonts like Times New Roman. Do not include illustrations of money bags or gold bullions or tacky design elements you see on low quality money-related websites.

```html
<!DOCTYPE html>
<html lang="en">
<head>
<meta charset="utf-8">
<title>Balance Transfer Banner – Card Match Scout</title>
<link rel="stylesheet" href="https://fonts.googleapis.com/css2?family=Arimo:wght@400;700&display=swap">
<style>
  :root {
    --brand-blue: #1c58a4;
    --ink: #333b47;
    --rule: #d9dde3;
    --row-alt: #f4f6f9;
    --rate-red: #c8362b;
    --cta-top: #fdb33b;
    --cta-bottom: #ee7a10;
    --cta-edge: #d8680a;
    --apply-top: #f9a33a;
    --apply-bottom: #e2620e;
    --canvas: #ffffff;
  }
  * { box-sizing: border-box; margin: 0; padding: 0; }
  html, body { width: 1200px; height: 148px; overflow: hidden; background: var(--canvas); }
  body { font-family: "Arimo", Arial, sans-serif; }

  .banner { position: relative; width: 1200px; height: 148px; overflow: hidden; background: var(--canvas); }

  .headline {
    position: absolute; left: 18px; top: 10px; width: 368px;
    color: var(--brand-blue); font-weight: 700; font-size: 28px; line-height: 38px;
    letter-spacing: -0.3px; white-space: nowrap;
  }

  .comparison-table {
    position: absolute; left: 392px; top: 0; width: 300px; height: 148px;
    border-left: 1px solid var(--rule); border-right: 1px solid var(--rule);
    font-size: 6px; color: var(--ink); box-shadow: 0 0 6px rgba(0,0,0,0.08);
  }
  .table-row {
    display: grid; grid-template-columns: 56px 76px 28px 28px 36px 16px 18px 34px;
    align-items: center; height: 48px; border-bottom: 1px solid var(--rule); padding-right: 4px;
  }
  .table-row:nth-child(even) { background: var(--row-alt); }
  .card-thumb { width: 40px; height: 27px; margin-left: 8px; border-radius: 3px; }
  .thumb-gold { background: linear-gradient(135deg, #e8c66a, #b8902d); }
  .thumb-silver { background: linear-gradient(135deg, #dfe4ea, #9aa4b0); }
  .thumb-blue { background: linear-gradient(135deg, #4f86c9, #1c4a86); }
  .offer-text { line-height: 7px; padding-right: 4px; }
  .offer-text strong { color: var(--rate-red); display: block; }
  .cell { text-align: center; }
  .apply-btn {
    justify-self: end; width: 28px; height: 12px; border-radius: 2px;
    background: linear-gradient(var(--apply-top), var(--apply-bottom));
    color: #fff; font-weight: 700; font-size: 6px; line-height: 12px; text-align: center;
  }

  .offers-intro {
    position: absolute; left: 714px; top: 38px;
    color: var(--brand-blue); font-size: 23px; letter-spacing: -0.2px; white-space: nowrap;
  }
  .brand-lockup {
    position: absolute; left: 714px; top: 80px; display: flex; align-items: center; gap: 10px;
    white-space: nowrap;
  }
  .brand-mark { width: 26px; height: 26px; background: var(--brand-blue); }
  .brand-name { color: var(--brand-blue); font-weight: 700; font-size: 24px; letter-spacing: -0.4px; }

  .cta-button {
    position: absolute; left: 986px; top: 28px; width: 196px; height: 92px;
    border: 2px solid var(--cta-edge); border-radius: 10px;
    background: linear-gradient(var(--cta-top), var(--cta-bottom));
    color: #fff; font-weight: 700; font-size: 30px; line-height: 35px; white-space: nowrap;
    display: flex; align-items: center; justify-content: center; text-align: center;
    text-shadow: 0 1px 2px rgba(120,50,0,0.45);
    box-shadow: inset 0 2px 0 rgba(255,255,255,0.45), 0 2px 4px rgba(0,0,0,0.2);
    text-decoration: none;
  }
</style>
</head>
<body>
<div class="banner">
  <h1 class="headline">Save up to $1,000 or more<br>in interest with a Balance<br>Transfer Credit Card.</h1>

  <div class="comparison-table">
    <div class="table-row">
      <div class="card-thumb thumb-gold" role="img" aria-label="Credit card image"></div>
      <div class="offer-text"><strong>Editor's Choice</strong>Low Rate Card</div>
      <div class="cell">0.00%</div>
      <div class="cell">13.99%</div>
      <div class="cell">0% for 6 mths</div>
      <div class="cell">$0</div>
      <div class="cell">55</div>
      <div class="apply-btn">Apply</div>
    </div>
    <div class="table-row">
      <div class="card-thumb thumb-silver" role="img" aria-label="Credit card image"></div>
      <div class="offer-text"><strong>0% Balance</strong>Transfer offer</div>
      <div class="cell">0.00%</div>
      <div class="cell">19.74%</div>
      <div class="cell">0% for 9 mths</div>
      <div class="cell">$49</div>
      <div class="cell">44</div>
      <div class="apply-btn">Apply</div>
    </div>
    <div class="table-row">
      <div class="card-thumb thumb-blue" role="img" aria-label="Credit card image"></div>
      <div class="offer-text"><strong>Low fee</strong>card for everyday</div>
      <div class="cell">2.99%</div>
      <div class="cell">17.99%</div>
      <div class="cell">3% for 12 mths</div>
      <div class="cell">$29</div>
      <div class="cell">55</div>
      <div class="apply-btn">Apply</div>
    </div>
  </div>

  <p class="offers-intro">Compare the offers on</p>
  <div class="brand-lockup">
    <span class="brand-mark"></span>
    <span class="brand-name">Card Match Scout</span>
  </div>

  <a class="cta-button" href="http://www.cardmatchscout.example.au">Compare<br>cards now</a>
</div>
</body>
</html>
```